Calm Fern Healthcare- Aged Care and Community Services

Looking for brochure to advertise our services. I will attach a draft that we do not want to use. Looking for graphics that are as natural as possible to present a personalised service. We supply services to aged people and people with disability. Please make it look classy and professional at the same time. I am looking for creativity. I have also attached the logo. Site addresses can be the last page. ideally looking for 2 designs, one A4 and another smaller possibly DL. Looking for creative out of the box thinkers. Thank you.

Target Market(s)

Aged Care service providers, disability service providers and private hospitals

Font styles to use
Serif
Sans Serif
Script

Colors
6b449b
886aae
eea4c8
f59195
fac994
3176b5
0555a3
cedeed
e4daeb

Requirements
Must have
• Targeted imagery, content and contact details
Nice to have
• personal profiles of people happy with our services

```html
<!DOCTYPE html>
<html lang="en">
<head>
<meta charset="utf-8">
<title>Calm Fern Healthcare – Brochure</title>
<link href="https://fonts.googleapis.com/css2?family=Roboto+Slab:wght@400;600;700;800&family=Roboto:wght@400;500;700&display=swap" rel="stylesheet">
<style>
:root{
  --bg:#e7dcec;
  --pink:#e0197d;
  --pink-soft:#f06aa8;
  --magenta:#c8207f;
  --purple:#8b3fb8;
  --violet:#6b449b;
  --ink:#1f1f1f;
  --dark:#2a2a2a;
  --grey:#5b5b5b;
  --lilac:#efe6f4;
  --lilac-2:#dccbe8;
  --white:#ffffff;
  --text:#333333;
  --serif:"Roboto Slab", Georgia, serif;
  --sans:"Roboto", Arial, sans-serif;
}
*{box-sizing:border-box;margin:0;padding:0}
html,body{width:1200px;height:3371px;overflow:hidden}
body{background:var(--bg);font-family:var(--serif);color:var(--text);position:relative}

.page{position:absolute;width:440px;height:622px;overflow:hidden;background:var(--white);box-shadow:0 12px 30px rgba(80,40,100,.18)}
.spread{position:absolute;left:160px;width:880px;height:622px;box-shadow:0 14px 34px rgba(80,40,100,.2)}
.spread .page{box-shadow:none;top:0}
.spread .left{left:0}
.spread .right{left:440px}
.spread .right::before{content:"";position:absolute;left:0;top:0;width:24px;height:100%;background:linear-gradient(90deg,rgba(0,0,0,.12),rgba(0,0,0,0));z-index:5}

/* ---------- cover ---------- */
.cover-top{position:absolute;inset:0 0 auto 0;height:260px;background:var(--ink)}
.cover-photo{position:absolute;left:0;top:150px;width:440px;height:400px;border-top-right-radius:90px;
  background:linear-gradient(135deg,#f3c3d8 0%,#e58ab7 40%,#c24e94 75%,#9a3d8f 100%)}
.cover-title{position:absolute;right:22px;top:30px;text-align:right;font-family:var(--serif);font-weight:800;line-height:1;font-size:42px;color:var(--white)}
.cover-title .accent{display:block;color:var(--pink)}
.cover-bottom{position:absolute;left:0;top:540px;width:440px;height:82px;background:var(--white);border-top-right-radius:40px}
.cover-blob{position:absolute;left:0;top:410px;width:290px;height:150px}
.brand-mark{position:absolute;font-family:var(--serif);font-weight:600;color:var(--white);font-size:17px;display:flex;align-items:center;gap:8px;white-space:nowrap}
.brand-mark .dot{width:12px;height:12px;border-radius:50%;background:var(--white);flex:none}
.cover .brand-mark{left:28px;top:470px}
.cover-contact{position:absolute;left:215px;top:560px;font-family:var(--serif);color:var(--ink)}
.cover-contact .phone{display:flex;align-items:center;gap:8px;font-size:20px;font-weight:700}
.cover-contact .phone svg{width:20px;height:20px;fill:var(--pink)}
.cover-contact .web{font-size:10px;margin:4px 0 0 28px}

/* ---------- common text ---------- */
.h2{font-family:var(--serif);font-weight:700;color:var(--ink);font-size:19px;line-height:1.05;text-transform:uppercase}
.h2::after{content:"";display:block;width:60px;height:3px;background:var(--pink);margin-top:6px}
.h3{font-family:var(--serif);font-weight:700;color:var(--pink);font-size:9px;text-transform:uppercase;margin:10px 0 4px}
.body{font-family:var(--serif);font-size:7.4px;line-height:1.6;color:var(--text)}
.body p+p{margin-top:7px}
.photo{position:absolute}

/* ---------- spread 1 ---------- */
.about-page{background:linear-gradient(160deg,#f7f0fa 0%,#eadcf2 55%,#e3cfee 100%)}
.about-card{position:absolute;left:26px;top:44px;width:330px;height:300px;background:rgba(255,255,255,.93);border-radius:24px;padding:22px 22px}
.about-card .body{margin-top:12px}
.employ-title{position:absolute;left:18px;top:338px;width:130px;text-align:center;font-family:var(--serif);font-weight:700;font-size:19px;color:var(--violet);line-height:1.05;text-transform:uppercase}
.employ-note{position:absolute;left:22px;top:400px;width:122px;text-align:center;font-family:var(--sans);font-weight:700;font-size:6.6px;line-height:1.5;color:var(--ink);text-transform:uppercase}
.employ-panel{position:absolute;left:150px;top:330px;width:270px;height:258px;border-radius:0 26px 0 0;background:linear-gradient(160deg,#e0197d 0%,#c3208a 60%,#9b3aa8 100%);padding:20px 18px;color:var(--white)}
.employ-panel .body{color:var(--white)}
.employ-panel ul{list-style:none;margin-top:10px}
.employ-panel li{font-size:7.2px;line-height:1.95;display:flex;align-items:center;gap:6px}
.employ-panel li::before{content:"";width:6px;height:6px;border:1px solid var(--white);border-radius:50%;flex:none}
.employ-rule{position:absolute;left:144px;top:330px;width:3px;height:258px;background:var(--pink)}

.partner-page{background:linear-gradient(180deg,#f5eef8,#eadff1)}
.partner-card{position:absolute;left:145px;top:36px;width:282px;height:370px;background:var(--white);border-radius:30px;padding:22px 24px 0 26px}
.believe{position:absolute;left:0;top:414px;width:440px;height:208px;background:linear-gradient(110deg,#e0197d 0%,#b52a95 55%,#7f3fb0 100%);padding:22px 64px 0 64px;color:var(--white)}
.believe .h2{color:var(--white);font-size:15px}
.believe .h2::after{background:var(--white)}
.believe p{font-family:var(--serif);font-size:9.2px;line-height:1.5;margin-top:12px}

/* ---------- spread 2 ---------- */
.benefits-page{background:linear-gradient(180deg,#f7f1fa,#ecdff3)}
.benefits-card{position:absolute;left:150px;top:22px;width:278px;height:262px;background:var(--white);border-radius:30px;padding:22px 22px}
.benefits-card .h3{margin-top:8px}
.roi{position:absolute;left:0;top:300px;width:440px;height:240px;background:linear-gradient(110deg,#d81b7d 0%,#b8248f 55%,#8a3ab2 100%);padding:22px 30px;color:var(--white)}
.roi .title{font-family:var(--serif);font-weight:700;font-size:15px;text-transform:uppercase}
.roi .sub{font-family:var(--serif);font-weight:700;font-size:11px;margin:10px 0 6px}
.roi p{font-family:var(--serif);font-size:7.6px;line-height:1.6}

.grow-page{background:linear-gradient(180deg,#f1e6f6,#e4d2ef)}
.resident{position:absolute;left:0;top:0;width:440px;height:176px;background:var(--dark);border-bottom-left-radius:60px;padding:28px 30px 0 40px}
.resident .title{font-family:var(--serif);font-weight:700;color:var(--pink);font-size:17px;line-height:1.05;text-transform:uppercase}
.resident p{font-family:var(--serif);font-size:8px;line-height:1.55;color:var(--white);text-transform:uppercase;margin-top:12px;max-width:330px}
.grow-title{position:absolute;left:40px;top:200px;font-family:var(--serif);font-weight:800;font-size:17px;color:var(--ink);text-transform:uppercase;line-height:1.05}
.tile{position:absolute;width:170px;height:104px;border-radius:14px;border:3px solid var(--white);box-shadow:0 4px 10px rgba(100,40,120,.2)}
.tile-label{position:absolute;background:var(--pink);color:var(--white);font-family:var(--serif);font-weight:700;font-size:7px;text-transform:uppercase;padding:4px 8px;line-height:1.3;border-radius:2px;z-index:2}

/* ---------- spread 3 (back) ---------- */
.back-page{background:var(--white)}
.vision{position:absolute;left:40px;top:60px;width:370px}
.vision-head{display:flex;align-items:center;gap:40px}
.vision-icon{width:52px;height:38px;flex:none}
.vision .title{font-family:var(--serif);font-weight:800;font-size:17px;color:var(--ink);text-transform:uppercase;margin-top:22px}
.vision p{font-family:var(--serif);font-size:7.8px;line-height:1.6;color:var(--text);margin:12px 0 0 92px}
.talk{position:absolute;left:0;top:310px;width:440px;height:312px;background:var(--dark)}
.talk-side{position:absolute;left:0;top:0;width:170px;height:312px;background:var(--grey);padding:34px 18px}
.talk-side .title{font-family:var(--serif);font-weight:700;font-size:15px;color:var(--white);text-transform:uppercase}
.talk-side .brand-mark{position:static;margin-top:60px;font-size:12px}
.talk-rule{position:absolute;left:178px;top:60px;width:3px;height:200px;background:var(--pink)}
.talk-info{position:absolute;left:196px;top:60px;width:230px;color:var(--white);font-family:var(--serif)}
.talk-info .phone{display:flex;align-items:center;gap:8px;font-size:18px;font-weight:700}
.talk-info .phone svg{width:18px;height:18px;fill:var(--pink)}
.talk-info .email{font-size:7.6px;margin:4px 0 0 26px}
.talk-info .city{color:var(--pink);font-weight:700;font-size:9px;text-transform:uppercase;margin-top:18px}
.talk-info .addr{font-size:8px;line-height:1.5}
</style>
</head>
<body>

<!-- Front cover -->
<section class="page cover" style="left:380px;top:177px" aria-label="Front cover">
  <div class="cover-top"></div>
  <div class="cover-photo" role="img" aria-label="Photo: elderly woman smiling with a caring nurse"></div>
  <h1 class="cover-title"><span class="accent">Reimagining</span><span>Healthcare</span></h1>
  <div class="cover-bottom"></div>
  <svg class="cover-blob" viewBox="0 0 290 150" aria-hidden="true">
    <defs><linearGradient id="blobA" x1="0" y1="1" x2="1" y2="0"><stop offset="0" stop-color="#7f3fb0"/><stop offset="1" stop-color="#e0197d"/></linearGradient></defs>
    <path d="M0 24 Q0 0 36 6 L210 28 Q275 38 282 96 Q288 150 230 150 L0 150 Z" fill="url(#blobA)"/>
  </svg>
  <div class="brand-mark"><span class="dot"></span>Calm Fern Healthcare</div>
  <div class="cover-contact">
    <div class="phone"><svg viewBox="0 0 24 24"><path d="M6.6 10.8a15.1 15.1 0 0 0 6.6 6.6l2.2-2.2c.3-.3.7-.4 1-.2 1.1.4 2.3.6 3.6.6.6 0 1 .4 1 1V20c0 .6-.4 1-1 1A17 17 0 0 1 3 4c0-.6.4-1 1-1h3.5c.6 0 1 .4 1 1 0 1.3.2 2.5.6 3.6.1.3 0 .7-.2 1z"/></svg>(08) 9400 7125</div>
    <div class="web">calmfernhealthcare.com.au</div>
  </div>
</section>

<!-- Spread 1: About / Why partner -->
<section class="spread" style="top:976px" aria-label="Inside spread: about us">
  <div class="page left about-page">
    <svg style="position:absolute;left:0;top:0;width:440px;height:622px" viewBox="0 0 440 622" aria-hidden="true">
      <defs><linearGradient id="blobB" x1="0" y1="0" x2="1" y2="1"><stop offset="0" stop-color="#f06aa8"/><stop offset="1" stop-color="#c3208a"/></linearGradient>
      <linearGradient id="blobC" x1="0" y1="0" x2="1" y2="1"><stop offset="0" stop-color="#b06fd0"/><stop offset="1" stop-color="#8b3fb8"/></linearGradient></defs>
      <path d="M300 0 L440 0 L440 110 Q400 140 350 110 Q300 80 300 30 Z" fill="url(#blobB)"/>
      <path d="M0 0 L110 0 Q90 50 40 60 Q10 66 0 90 Z" fill="url(#blobC)" opacity=".55"/>
      <path d="M0 520 Q40 500 80 540 Q120 580 140 622 L0 622 Z" fill="url(#blobC)"/>
      <path d="M400 260 Q440 250 440 290 L440 420 Q420 400 405 360 Q390 300 400 260 Z" fill="url(#blobB)"/>
    </svg>
    <div class="about-card">
      <h2 class="h2">About us</h2>
      <div class="body">
        <p>Calm Fern Healthcare is a Perth based staffing solutions provider which thrives to partner with organisations in meeting their continuing resource requirements. We are slowly building a reputation on our responsiveness to client enquiries, whilst meeting our key service deliverables. We work with service providers in Residential Aged Care, Community Supports and Hospitals.</p>
        <p>We believe in the key to building lasting relationships in life to have a willingness and ability to reciprocity which we aim to do by understanding the intricate needs of our clients, collaboratively identify problems, help them progress from their current situation, earn trust and thrive for excellence.</p>
        <p>Our vision is to be the most responsive staffing solution provider in WA, whilst sourcing and placing staff that hold strong values which include ethics, accountability, respect, integrity and adaptable. Our mission is to partner with like-minded organisations that genuinely thrive in making a difference, are ethically placed in society and have effective governance at the care of their operations.</p>
      </div>
    </div>
    <div class="employ-title">Who we employ?</div>
    <div class="employ-note">Our diverse database of skilled staff gives you the peace of mind you need to do what you do best, look after your customers.</div>
    <div class="employ-rule"></div>
    <div class="employ-panel">
      <div class="body">We actively source and recruit skills professionals with direct cultural fit to most of our clients. These roles include but are not limited to:</div>
      <ul>
        <li>Registered Nurses</li>
        <li>Enrolled Nurses</li>
        <li>Nursing Assistants/Carers</li>
        <li>Allied Health Assistants (Physiotherapy &amp; OT)</li>
        <li>Chefs and Cooks (healthcare experienced)</li>
        <li>Catering Staff and Kitchen hands</li>
        <li>Cleaning and Domestic Assistants</li>
        <li>Laundry Attendant and</li>
        <li>many more related professionals</li>
      </ul>
    </div>
  </div>
  <div class="page right partner-page">
    <div class="photo" role="img" aria-label="Photo: nurse in white uniform with arms folded" style="left:0;top:0;width:160px;height:414px;background:linear-gradient(180deg,#f4e8ef 0%,#e9d6e6 50%,#d9c3e0 100%)"></div>
    <div class="partner-card">
      <h2 class="h2">Why partner<br>with us</h2>
      <div class="h3" style="margin-top:14px">Service design</div>
      <div class="body">Prior to placing all staff, we ensure we have conducted a full client profile to understand your business needs, to end-to-end operations, service delivery, P/R and governance. This will enable us to design a service around your specific needs which allows for a seamless integration. We encourage continuity of service delivery which we implement by ensuring the same staff are placed at your sites. Culturally, this enables our staff to build relationships with your teams and customers allowing for a natural fit.</div>
      <div class="h3" style="margin-top:14px">Technology</div>
      <div class="body">We have integrated our systems with necessary technology as we believe technology is a part of modern day efficiencies. People are our business and nothing can replace human relationships, interactions or connection however to effectively enhance these human related characteristics, technology helps us in maximising efficiencies and minimising error. Our on-boarding and scheduling platforms are automated, further solidifying compliance and managing risk.</div>
    </div>
    <div class="believe">
      <h2 class="h2">What we believe</h2>
      <p>A person who is appreciated, always does more than what is expected. Our staff are at the centre of all our decisions as we are only as good as the people we hire. If we look after our staff, they will look after our client.</p>
    </div>
  </div>
</section>

<!-- Spread 2: Benefits / Growth -->
<section class="spread" style="top:1775px" aria-label="Inside spread: partnership benefits">
  <div class="page left benefits-page">
    <div class="photo" role="img" aria-label="Photo: smiling nurse in white uniform" style="left:0;top:0;width:230px;height:300px;background:linear-gradient(160deg,#f6ecf1 0%,#ead8e6 60%,#dcc6e2 100%)"></div>
    <div class="benefits-card">
      <h2 class="h2" style="font-size:16px">Key partnership<br>benefits</h2>
      <div class="h3">Financial</div>
      <div class="body">A partnership with Calm Fern will enhance your margins and profitability allowing you to put more money towards care.</div>
      <div class="h3">Service delivery improvements</div>
      <div class="body">Enhanced customer choice and flexibility as well as improved customer outcomes.</div>
      <div class="h3">Risk management enhancements</div>
      <div class="body">You have the option of outsourcing workcover and cost.</div>
      <div class="h3">Operational efficiencies</div>
      <div class="body">Improved organisational efficiencies and optimisation of the workforce.</div>
    </div>
    <div class="roi">
      <div class="title">The real return of investment</div>
      <div class="sub">Patient Satisfaction</div>
      <p>The more your clients are satisfied, the more they are capable of promoting your brand, speaking highly of your service delivery during accreditation and ultimately the more they feel you value them as individuals. The national care standards body relentlessly seeks evidence of compassionate, complaint and effective corporate and clinical governance. By embedding these standards into each policy, process and service implementation to evaluation, the more you will have peace of mind should any regulatory department decide to pay you a visit. We are here to ensure we align to your standard whilst being adaptable to the changing nature of the industry we operate in.</p>
    </div>
  </div>
  <div class="page right grow-page">
    <div class="resident">
      <div class="title">Redesigning resident<br>experiences</div>
      <p>We value feedback and we consistency seek it as it help us grow. Service delivery and feedback are a match that cannot be unweeded.</p>
    </div>
    <div class="grow-title">Retaining customers<br>&amp; how we grow</div>
    <div class="tile" role="img" aria-label="Photo: doctors greeting an older patient" style="left:40px;top:290px;background:linear-gradient(135deg,#e9eef5,#c9d6e6)"></div>
    <div class="tile-label" style="left:48px;top:272px">Ensure positive<br>first encounters</div>
    <div class="tile" role="img" aria-label="Photo: nurse caring for an elderly man" style="left:236px;top:350px;background:linear-gradient(135deg,#f2e9ee,#d8c6d8)"></div>
    <div class="tile-label" style="left:286px;top:458px">Maintain<br>professionalism</div>
    <div class="tile" role="img" aria-label="Photo: clinician using medical equipment" style="left:120px;top:470px;background:linear-gradient(135deg,#6b7ea8,#2f3f6e)"></div>
    <div class="tile-label" style="left:40px;top:448px">Continue training<br>and development</div>
  </div>
</section>

<!-- Spread 3: Back and front cover -->
<section class="spread" style="top:2574px" aria-label="Back and front cover">
  <div class="page left back-page">
    <div class="vision">
      <div class="vision-head">
        <svg class="vision-icon" viewBox="0 0 52 38" aria-hidden="true">
          <path d="M2 6 V2 H8 M44 2 H50 V6 M50 32 V36 H44 M8 36 H2 V32" fill="none" stroke="#e0197d" stroke-width="2"/>
          <path d="M8 19 Q26 2 44 19 Q26 36 8 19 Z" fill="none" stroke="#1f1f1f" stroke-width="2"/>
          <circle cx="26" cy="19" r="6" fill="none" stroke="#1f1f1f" stroke-width="2"/>
        </svg>
        <div class="title">The vision</div>
      </div>
      <p>Our vision is to be the most responsive staffing solutions provider in WA and SA. We thrive to attract, place and retain staff with shared values which include ethics, integrity, respect and accountability. We will continually adapt to the changing needs of our sector and environment to ensure we exceed at all times our partnership expectations.</p>
    </div>
    <div class="talk">
      <div class="talk-side">
        <div class="title">Talk to us</div>
        <div class="brand-mark"><span class="dot"></span>Calm Fern Healthcare</div>
      </div>
      <div class="talk-rule"></div>
      <div class="talk-info">
        <div class="phone"><svg viewBox="0 0 24 24"><path d="M6.6 10.8a15.1 15.1 0 0 0 6.6 6.6l2.2-2.2c.3-.3.7-.4 1-.2 1.1.4 2.3.6 3.6.6.6 0 1 .4 1 1V20c0 .6-.4 1-1 1A17 17 0 0 1 3 4c0-.6.4-1 1-1h3.5c.6 0 1 .4 1 1 0 1.3.2 2.5.6 3.6.1.3 0 .7-.2 1z"/></svg>08 9400 7125</div>
        <div class="email">admin@calmfernhealthcare.com.au</div>
        <div class="city">Perth</div>
        <div class="addr">14 Banksia Lane, Ashmere WA 6190</div>
        <div class="city">Adelaide</div>
        <div class="addr">Level 1, 8 Orchard Street,<br>Ridgeleigh SA 5090</div>
      </div>
    </div>
  </div>
  <div class="page right cover">
    <div class="cover-top"></div>
    <div class="cover-photo" role="img" aria-label="Photo: elderly woman smiling with a caring nurse"></div>
    <h1 class="cover-title"><span class="accent">Reimagining</span><span>Healthcare</span></h1>
    <div class="cover-bottom"></div>
    <svg class="cover-blob" viewBox="0 0 290 150" aria-hidden="true">
      <path d="M0 24 Q0 0 36 6 L210 28 Q275 38 282 96 Q288 150 230 150 L0 150 Z" fill="url(#blobA)"/>
    </svg>
    <div class="brand-mark"><span class="dot"></span>Calm Fern Healthcare</div>
    <div class="cover-contact">
      <div class="phone"><svg viewBox="0 0 24 24"><path d="M6.6 10.8a15.1 15.1 0 0 0 6.6 6.6l2.2-2.2c.3-.3.7-.4 1-.2 1.1.4 2.3.6 3.6.6.6 0 1 .4 1 1V20c0 .6-.4 1-1 1A17 17 0 0 1 3 4c0-.6.4-1 1-1h3.5c.6 0 1 .4 1 1 0 1.3.2 2.5.6 3.6.1.3 0 .7-.2 1z"/></svg>(08) 9400 7125</div>
      <div class="web">calmfernhealthcare.com.au</div>
    </div>
  </div>
</section>

</body>
</html>
```